Pelwick Renovations Letterhead

Pelwick does not do actual renovation, but rather handles high end project management of renovation (primarily residential with an eye toward commercial and International) The renovation work could look very different between projects. This company works directly with the clients and manages the work of contractors, architects and interior designers (either subcontracted directly by Pelwick or hired by the client and entrusted to Pelwick to manage). Clients are high end in the economic scale and all materials should speak to that audience. Provoke a sense of change, openness and imagination, trust and integrity. The owner is female, but the audience will be heavily slanted male. It should not be a "feminine" or "masculine" looking . If anything, slant more on the masculine side.

Clean, simple, yet creative and artistically appealing. The logo should be clear and not competing with too many surrounding design elements.

There is a contest also on for business card. Please check that section if you would like to compete for both.

Get your creative juices going!

Target Market(s)

High end cients. Additional audience: professionals (architects, etc...) designers, contractors

Industry/Entity Type

Residential

Requirements
Must have
• Logo must be included in all materials

```html
<!DOCTYPE html>
<html lang="en">
<head>
<meta charset="utf-8">
<title>Pelwick Renovations Letterhead</title>
<link href="https://fonts.googleapis.com/css2?family=Jost:wght@600&family=Noto+Sans:wght@400&display=swap" rel="stylesheet">
<style>
  :root {
    --paper: #ffffff;
    --page-bg: #e9e9e9;
    --ink: #1d1d1d;
    --accent: #38e28f;
    --rule: #333333;
  }
  html, body {
    margin: 0;
    padding: 0;
    overflow: hidden;
    background: var(--page-bg);
  }
  .letterhead {
    position: relative;
    width: 946px;
    height: 1200px;
    background: linear-gradient(90deg, #f1f1f1 0%, var(--paper) 28%);
    overflow: hidden;
    font-family: "Noto Sans", sans-serif;
    color: var(--ink);
  }
  .brand {
    position: absolute;
    left: 22px;
    top: 94px;
    display: flex;
    align-items: center;
    gap: 10px;
    font-family: "Jost", sans-serif;
    font-weight: 600;
    font-size: 22px;
    letter-spacing: 0.5px;
    color: var(--ink);
  }
  .brand-mark {
    width: 12px;
    height: 12px;
    background: var(--accent);
  }
  .contact {
    position: absolute;
    left: 614px;
    top: 33px;
    height: 83px;
    border-left: 1.5px solid var(--rule);
    padding-left: 17px;
    font-size: 16px;
    line-height: 21.5px;
  }
  .contact-row {
    display: flex;
    align-items: center;
    gap: 6px;
    white-space: nowrap;
  }
  .contact-icon {
    width: 12px;
    height: 12px;
    flex: none;
  }
  .footer-wave {
    position: absolute;
    left: 0;
    top: 0;
  }
  .address {
    position: absolute;
    left: 683px;
    top: 1132px;
    transform: translateX(-50%);
    text-align: center;
    color: #ffffff;
    font-size: 17px;
    line-height: 22px;
    white-space: nowrap;
  }
</style>
</head>
<body>
<main class="letterhead">
  <header class="brand">
    <span class="brand-mark"></span>
    <span class="brand-name">PELWICK RENOVATIONS</span>
  </header>

  <address class="contact" style="font-style:normal">
    <div class="contact-row">
      <svg class="contact-icon" viewBox="0 0 12 12"><path d="M3 1 L5 3.5 L4 5 Q5 7.5 7 8 L8.5 7 L11 9 L9.5 11 Q3 10 1 3 Z" fill="none" stroke="#1d1d1d" stroke-width="1.2"/></svg>
      <span>555-014-2290</span>
    </div>
    <div class="contact-row">
      <svg class="contact-icon" viewBox="0 0 12 12"><path d="M3 1 L5 3.5 L4 5 Q5 7.5 7 8 L8.5 7 L11 9 L9.5 11 Q3 10 1 3 Z" fill="none" stroke="#1d1d1d" stroke-width="1.2"/></svg>
      <span>021 884 319</span>
    </div>
    <div class="contact-row">
      <svg class="contact-icon" viewBox="0 0 12 12"><path d="M1 5 L6 1.5 L11 5 V10.5 H1 Z" fill="#1d1d1d"/><path d="M1.5 5.5 L6 8.5 L10.5 5.5" fill="none" stroke="#fff" stroke-width="1"/></svg>
      <span>pelwickrenovations@mailbox.com</span>
    </div>
    <div class="contact-row">
      <svg class="contact-icon" viewBox="0 0 12 12"><circle cx="6" cy="6" r="5" fill="none" stroke="#1d1d1d" stroke-width="1.1"/><ellipse cx="6" cy="6" rx="2.2" ry="5" fill="none" stroke="#1d1d1d" stroke-width="1"/><path d="M1 6 H11 M2 3.5 H10 M2 8.5 H10" stroke="#1d1d1d" stroke-width="0.9"/></svg>
      <span>www.pelwickrenovations.com</span>
    </div>
  </address>

  <svg class="footer-wave" width="946" height="1200" viewBox="0 0 946 1200" aria-hidden="true">
    <path d="M0,939 C10,1060 120,1125 260,1128 C340,1130 400,1118 447,1109 C540,1098 610,1093 680,1093 C800,1093 880,1130 946,1190 L946,1200 L0,1200 Z" fill="var(--ink)"/>
    <path d="M6,1045 C50,1120 140,1152 240,1152 C400,1152 520,1096 680,1096 C790,1096 870,1130 930,1182" fill="none" stroke="#ffffff" stroke-width="20"/>
    <path d="M6,1045 C50,1120 140,1152 240,1152 C400,1152 520,1096 680,1096 C790,1096 870,1130 930,1182" fill="none" stroke="var(--accent)" stroke-width="12"/>
  </svg>

  <address class="address" style="font-style:normal">
    <div>Street Name, City Name</div>
    <div>State Zip Code</div>
  </address>
</main>
</body>
</html>
```